Maple Ridge business card design

Card needs to include the following text/items:
Company Logo
Tobin Marsh
Phone # - 555-318-7642
service@mapleridgelandscaping.example
Lawn & landscape maintenance services

```html
<!DOCTYPE html>
<html lang="en">
<head>
<meta charset="utf-8">
<title>Maple Ridge Business Card</title>
<link href="https://fonts.googleapis.com/css2?family=Cinzel:wght@700&family=Montserrat:wght@600&display=swap" rel="stylesheet">
<style>
  :root {
    --backdrop: #e6e4df;
    --leaf: #5b8a3c;
    --leaf-dark: #2f5a1f;
    --rust: #9a3d1c;
    --rust-text: #8a3a1a;
    --paper: #eef3f8;
  }
  * { margin: 0; padding: 0; box-sizing: border-box; }
  html, body { width: 1200px; height: 1000px; overflow: hidden; }
  body { background: var(--backdrop); position: relative; font-family: "Montserrat", sans-serif; }

  .card { position: absolute; left: 355px; width: 490px; height: 278px; box-shadow: 0 3px 8px rgba(0,0,0,0.18); }
  .card--front { top: 170px; background: linear-gradient(to bottom, var(--leaf) 0 60%, var(--rust) 60% 100%); }
  .card--back  { top: 540px; background: linear-gradient(to bottom, var(--rust) 0 40%, var(--leaf) 40% 100%); }

  .panel { position: absolute; left: 28px; top: 28px; width: 435px; height: 223px; background: var(--paper); }
  .card--back .panel { top: 23px; height: 227px; }

  .brand { position: absolute; text-align: center; }
  .brand__mark { display: block; margin: 0 auto; border-radius: 50%; background: var(--leaf); }
  .brand__name { display: block; font-family: "Cinzel", serif; font-weight: 700; color: var(--leaf-dark); white-space: nowrap; }

  .card--front .brand { left: 12px; top: 62px; width: 128px; }
  .card--front .brand__mark { width: 80px; height: 80px; }
  .card--front .brand__name { font-size: 19px; margin-top: 6px; }

  .card--back .brand { left: 0; top: 36px; width: 435px; }
  .card--back .brand__mark { width: 104px; height: 104px; }
  .card--back .brand__name { font-size: 25px; margin-top: 6px; }

  .person { position: absolute; left: 172px; top: 66px; width: 222px; }
  .person__name { font-family: "Cinzel", serif; font-weight: 700; font-size: 31px; color: var(--leaf-dark); white-space: nowrap; line-height: 1; padding-bottom: 10px; border-bottom: 2px solid var(--rust); }

  .contact { position: absolute; left: 172px; list-style: none; color: var(--leaf-dark); display: flex; align-items: center; gap: 9px; }
  .contact svg { flex: none; }
  .contact--phone { top: 130px; font-size: 14px; }
  .contact--email { top: 170px; font-size: 10px; }

  .tagline { position: absolute; left: 0; top: 181px; width: 435px; text-align: center; font-family: "Cinzel", serif; font-weight: 700; font-size: 14px; color: var(--rust-text); }
</style>
</head>
<body>
  <section class="card card--front">
    <div class="panel">
      <div class="brand">
        <span class="brand__mark"></span>
        <span class="brand__name">Maple Ridge</span>
      </div>
      <div class="person"><h1 class="person__name">Tobin Marsh</h1></div>
      <div class="contact contact--phone">
        <svg width="18" height="18" viewBox="0 0 18 18" aria-hidden="true">
          <circle cx="9" cy="9" r="8" fill="none" stroke="var(--leaf-dark)" stroke-width="1.5"/>
          <path d="M6 5.2l1.4-.4 1 2.2-.9.7c.5 1 1.3 1.8 2.3 2.3l.7-.9 2.2 1-.4 1.4c-3.2.2-6.5-3.1-6.3-6.3z" fill="var(--leaf-dark)"/>
        </svg>
        <span>555-318-7642</span>
      </div>
      <div class="contact contact--email">
        <svg width="18" height="12" viewBox="0 0 18 12" aria-hidden="true">
          <rect width="18" height="12" fill="var(--leaf-dark)"/>
          <path d="M0 0l9 7 9-7" fill="none" stroke="var(--paper)" stroke-width="1.2"/>
        </svg>
        <span>service@mapleridgelandscaping.example</span>
      </div>
    </div>
  </section>

  <section class="card card--back">
    <div class="panel">
      <div class="brand">
        <span class="brand__mark"></span>
        <span class="brand__name">Maple Ridge</span>
      </div>
      <p class="tagline">Lawn &amp; landscape maintenance services</p>
    </div>
  </section>
</body>
</html>
```